Premium Wraparound Label Design for 6 oz Guava Butter Jar – Lanikeo Sweet Kitchen

Design a continuous wraparound label for an 6 oz circular glass jar that integrates the Lanikeo Sweet Kitchen logo (featuring the pink and brown leaf motif) and the Guava Butter nutrition label into one cohesive, premium presentation. The design should feel authentically Hawaiian, classic, and handcrafted—reflecting the brand’s legacy of island-inspired desserts.
Label Specifications
Container: 8 oz round glass jar
Label Type: Full wraparound (one continuous label)
Approximate Label Size: 2.5 inches tall × 8.5 inches wide
Finish: Matte or satin with optional gold foil highlights
Print: CMYK-ready artwork with bleed and safe zones clearly marked
Design Elements to Integrate
1. Front Panel (Main Display Area):
Prominently feature the Lanikeo Sweet Kitchen logo centered and scaled proportionally.
Display the product name “Guava Butter” in elegant, legible typography that complements the logo.
Add the following text beneath or near the product name:
“Made in Hawai‘i”
“Net Wt. 8 oz (227g)”
“Keep Refrigerated” (in smaller but clear type).
Background tones should complement the logo—cream, soft tan, or pastel pink for warmth and harmony.
The front should communicate island sophistication—premium yet inviting.
2. Side Panel (Transition Area):
Create a smooth visual transition around the jar using a subtle, continuous background pattern such as tropical leaves, ocean wave textures, or gold accent lines.
Include the brand story text:
“Lanikeo Sweet Kitchen brings authentic island flavors to every table. Our signature Guava Butter blends tropical fruit and fresh cream for a taste of pure aloha.”
3. Back Panel (Informational Area):
Integrate the Guava Butter nutrition facts panel and ingredients list (from the attached file).
Ensure layout is FDA-compliant, legible, and well-balanced.
Beneath the ingredients, include:
“Manufactured by Lanikeo Sweet Kitchen, Hawai‘i.”
“Keep Refrigerated.”
Leave space for:
A QR code linking to the brand website and social media.
A barcode area, placed neatly near the bottom or corner.
Aesthetic Direction
Style: Premium, classic, and island-inspired
Color Palette: Cream base with warm browns, muted pinks, and gold accents
Typography:
Serif or script for product name and logo (for a classic, handcrafted look)
Clean sans-serif for informational text
Mood: Heritage meets handcrafted luxury — nostalgic yet refined
Finish Options:
Matte for artisanal authenticity
Satin or metallic foil for a modern, premium touch
Deliverables
Designers should submit:
3 design variations (e.g., classic heritage, minimalist modern, and premium tropical).
Editable source files (AI, PSD, or layered PDF) with bleed and safe zones clearly marked.
Mockups on an 8 oz round glass jar for visual presentation.

Target Market(s)

Craft fair consumers / tourist in hawaii

Industry/Entity Type

food and Bev

Logo Text

see description

Font styles to use
Serif
Sans Serif
Script

Requirements
Must have
• see description
Nice to have
• see description
Should not have
• see description

```html
<!DOCTYPE html>
<html lang="en">
<head>
<meta charset="utf-8">
<title>Lanikeo Sweet Kitchen – Guava Butter Wraparound Label</title>
<link href="https://fonts.googleapis.com/css2?family=Cinzel:wght@500&family=Lobster&family=Montserrat:wght@400;600;700&display=swap" rel="stylesheet">
<style>
  :root {
    --page: #ffffff;
    --label-tan: #e9dfd2;
    --front-cream: #f3eee7;
    --brown: #5a3418;
    --rose: #d99a99;
    --rose-deep: #b9706f;
    --nf-light: #f2cfcc;
    --nf-mid: #d9a3a0;
    --ink: #2a1a12;
    --white: #ffffff;
  }
  * { margin: 0; padding: 0; box-sizing: border-box; }
  html, body { width: 1200px; height: 1200px; overflow: hidden; background: var(--page); }
  body { position: relative; font-family: "Montserrat", sans-serif; color: var(--brown); }

  .label {
    position: absolute; left: 241px; top: 494px; width: 718px; height: 212px;
    background: var(--label-tan);
  }
  .label-texture {
    position: absolute; inset: 0;
    background: linear-gradient(180deg, #ebe2d6 0%, #e6dccf 100%);
  }

  /* Back panel: nutrition facts */
  .nutrition {
    position: absolute; left: 29px; top: 13px; width: 89px; height: 186px;
    background: linear-gradient(160deg, var(--nf-light) 0%, var(--nf-mid) 55%, var(--nf-light) 100%);
    border: 1px solid var(--ink); padding: 2px 3px;
    color: var(--ink); font-size: 4.3px; line-height: 1.35;
  }
  .nutrition h2 { font-size: 10.5px; font-weight: 700; line-height: 1.1; border-bottom: 0.5px solid var(--ink); }
  .nutrition .serving { border-bottom: 2.5px solid var(--ink); padding-bottom: 1px; }
  .nutrition .amount { font-weight: 700; }
  .nutrition .calories { display: flex; justify-content: space-between; font-size: 8px; font-weight: 700; border-bottom: 1.5px solid var(--ink); line-height: 1.15; }
  .nutrition .dv { text-align: right; border-bottom: 0.5px solid var(--ink); }
  .nutrition .row { border-bottom: 0.5px solid var(--ink); }
  .nutrition .row.indent { padding-left: 4px; }
  .nutrition .row.indent2 { padding-left: 8px; }
  .nutrition .thick { border-bottom: 2.5px solid var(--ink); }
  .nutrition .ingredients { margin-top: 2px; }
  .nutrition b { font-weight: 700; }

  .maker {
    position: absolute; left: 120px; top: 74px; width: 130px;
    text-align: center; font-size: 7px; line-height: 1.4; color: var(--ink);
  }
  .maker .keep { margin-top: 18px; }

  .code-box {
    position: absolute; background: var(--white); border: 1px solid #6b5a4c;
  }
  .code-box.back { left: 167px; top: 163px; width: 67px; height: 32px; }
  .code-box.side { left: 558px; top: 107px; width: 82px; height: 82px; }

  /* Front panel */
  .front {
    position: absolute; left: 273px; top: 10px; width: 232px; height: 183px;
    background: var(--front-cream); text-align: center;
  }
  .brand-dot {
    display: block; width: 40px; height: 40px; margin: 12px auto 0;
    border-radius: 50%; background: var(--rose);
  }
  .brand-name {
    font-family: "Cinzel", serif; font-weight: 500; color: var(--brown);
    margin-top: 8px; line-height: 1.05;
  }
  .brand-name .line1 { display: block; font-size: 24px; letter-spacing: 1px; }
  .brand-name .line2 { display: block; font-size: 11px; letter-spacing: 1.5px; margin-top: 2px; }
  .est {
    display: flex; align-items: center; justify-content: center; gap: 6px;
    font-size: 5.5px; font-weight: 600; letter-spacing: 0.6px; margin-top: 6px; color: var(--brown);
  }
  .est::before, .est::after { content: ""; width: 14px; height: 1px; background: var(--brown); }
  .product-name {
    font-family: "Lobster", cursive; font-size: 38px; color: var(--rose);
    margin-top: 4px; line-height: 1;
  }
  .front-info {
    position: absolute; left: 286px; top: 193px; width: 205px;
    display: flex; justify-content: space-between;
    font-size: 7.5px; color: var(--ink);
  }
  .front-info span:first-child { margin-left: 1px; }

  /* Side panel: brand story */
  .story {
    position: absolute; left: 519px; top: 24px; width: 162px;
    font-size: 7.6px; line-height: 1.3; color: var(--brown);
  }
</style>
</head>
<body>
  <section class="label" aria-label="Guava Butter wraparound jar label">
    <div class="label-texture" role="img" aria-label="Soft cream background with flowing wave lines"></div>

    <div class="nutrition">
      <h2>Nutrition Facts</h2>
      <div class="serving">Serving Size 1 tbsp (15g)</div>
      <div class="amount">Amount Per Serving</div>
      <div class="calories"><span>Calories</span><span>150</span></div>
      <div class="dv">% Daily Value*</div>
      <div class="row"><b>Total Fat</b> 8g 10%</div>
      <div class="row indent">Saturated Fat 5g 25%</div>
      <div class="row indent">Trans Fat 0g</div>
      <div class="row"><b>Cholesterol</b> 45mg 15%</div>
      <div class="row"><b>Sodium</b> 5mg 0%</div>
      <div class="row"><b>Total Carbohydrate</b> 18g 7%</div>
      <div class="row indent">Dietary Fiber 0g 0%</div>
      <div class="row indent">Total Sugars 17g</div>
      <div class="row indent2">Includes 14g Added Sugars 28%</div>
      <div class="row thick"><b>Protein</b> 1g</div>
      <div class="row">Vit. D 0% · Calcium 2%</div>
      <div class="row">Iron 0% · Potassium 1%</div>
      <p class="ingredients"><b>Ingredients:</b> Guava Concentrate, Unsalted Butter (Cream, Natural Flavor), Cane Sugar, Whole Eggs, Egg Yolks, Pasteurized Blend of Natural Flavors and Spices.</p>
    </div>

    <div class="maker">
      <p>Manufactured by<br>Lanikeo Sweet Kitchen, Hawai‘i.</p>
      <p class="keep">Keep Refrigerated.</p>
    </div>
    <div class="code-box back" aria-label="Barcode area"></div>

    <div class="front">
      <span class="brand-dot" aria-hidden="true"></span>
      <div class="brand-name"><span class="line1">LANIKEO</span><span class="line2">SWEET KITCHEN</span></div>
      <div class="est">EST.1999</div>
      <div class="product-name">Guava Butter</div>
    </div>
    <div class="front-info"><span>Net Wt. 8 oz (227g)</span><span>Made in Hawai‘i</span></div>

    <p class="story">Lanikeo Sweet Kitchen brings authentic island flavors to every table. Our signature Guava Butter blends tropical fruit and fresh cream for a taste of pure aloha.</p>
    <div class="code-box side" aria-label="QR code area"></div>
  </section>
</body>
</html>
```